Safer Injecting Sites Poster for IV Drug Users

I need an A2-sized poster to help IV drug users understand which sites they can use on their body with minimal risk, and understand which areas are higher risk for complications. The poster is educational and should use clear images of anatomical areas/veins. The attached documents provides background information to help the designer understand the complexity of this issue. I've attached a sample image that gives an idea of what kind of information patients need to see to be engaging.

Target Market(s)

IV Drug Users

Font styles to use
Sans Serif

Requirements
Must have
• Simple imagery to help people understand where low risk and high risk injecting areas are. Must include advice on safe injecting techniques consistent with the section "Vein Care and Injecting Sites on the Body" and "Vein Care and the Circulatory System" from the Clean Practice Manual attached to brief.
Nice to have
• High quality imagery

```html
<!DOCTYPE html>
<html lang="en">
<head>
<meta charset="utf-8">
<title>Clean Practice Manual – Vein Care Poster</title>
<link href="https://fonts.googleapis.com/css2?family=Alfa+Slab+One&family=Montserrat:wght@500;600;700&family=Arimo:wght@400&display=swap" rel="stylesheet">
<style>
  :root {
    --page-bg: #f2f9fe;
    --poster-light: #e6f5fd;
    --poster-mid: #c4e7f9;
    --poster-deep: #93d2f2;
    --ink: #1a1a1a;
    --purple: #4b2a78;
    --purple-head: #5b2e8e;
    --figure-light: #e4eef6;
    --figure-vein: #9cc3e3;
    --leader: #d3204f;
  }
  * { margin: 0; padding: 0; box-sizing: border-box; }
  html, body { width: 803px; height: 1200px; overflow: hidden; background: var(--page-bg); }
  .canvas { position: relative; width: 803px; height: 1200px; }
  .poster {
    position: absolute; left: 21.5px; top: 331px;
    width: 1197px; height: 847px;
    transform: scale(0.6349); transform-origin: 0 0;
    background: linear-gradient(100deg, var(--poster-light) 0%, #f3fafe 40%, var(--poster-mid) 70%, var(--poster-deep) 100%);
    overflow: hidden;
    font-family: "Arimo", Arial, sans-serif;
    color: var(--ink);
  }
  .legend { position: absolute; left: 71px; top: 51px; font-size: 12.5px; line-height: 13px; }
  .vein-figure { position: absolute; left: 250px; top: 60px; width: 135px; height: 725px; }
  .leaders { position: absolute; left: 0; top: 0; width: 1197px; height: 847px; }
  .label { position: absolute; font-size: 12.5px; line-height: 11px; white-space: nowrap; }
  .label.l { text-align: right; }

  .brand { position: absolute; left: 53px; top: 706px; color: var(--purple); font-family: "Montserrat", sans-serif; font-weight: 700; }
  .brand-mark { display: flex; align-items: center; gap: 10px; font-size: 48px; line-height: 52px; }
  .brand-mark .dot { width: 22px; height: 22px; border-radius: 50%; background: var(--purple); }
  .brand-sub { display: inline-block; margin-left: 32px; font-size: 10.5px; line-height: 12px; padding-bottom: 2px; border-bottom: 2px solid var(--purple); }

  .content { position: absolute; left: 600px; top: 0; width: 560px; }
  .kicker { position: absolute; left: 18px; top: 56px; font-family: "Alfa Slab One", serif; font-size: 22px; line-height: 28px; color: var(--purple); white-space: nowrap; }
  .title { position: absolute; font-family: "Alfa Slab One", serif; font-size: 56px; line-height: 60px; color: var(--purple); white-space: nowrap; font-weight: 400; }
  .title.one { left: -30px; top: 88px; }
  .title.two { left: 0; top: 146px; }
  .welcome-head { position: absolute; top: 256px; font-family: "Montserrat", sans-serif; font-weight: 600; font-size: 15.8px; white-space: nowrap; }
  .welcome-body { position: absolute; top: 282px; width: 550px; font-family: "Montserrat", sans-serif; font-weight: 500; font-size: 11.6px; line-height: 13.8px; }
  .section-head { position: absolute; font-family: "Montserrat", sans-serif; font-weight: 700; font-size: 16px; line-height: 20px; color: var(--purple-head); white-space: nowrap; }
  .small { position: absolute; width: 560px; font-family: "Montserrat", sans-serif; font-weight: 500; font-size: 8.6px; line-height: 10.5px; }
  .small strong { font-weight: 700; font-size: 9.6px; }
  .checks { position: absolute; top: 491px; display: grid; grid-template-columns: 233px 200px; row-gap: 8px; }
  .check { display: flex; align-items: center; gap: 7px; font-family: "Montserrat", sans-serif; font-weight: 600; font-size: 14px; line-height: 19px; color: var(--purple-head); }
  .check svg { width: 14px; height: 14px; }
  .bullet { position: absolute; width: 330px; padding-left: 8px; text-indent: -8px; font-family: "Montserrat", sans-serif; font-weight: 500; font-size: 8.6px; line-height: 10.5px; }
</style>
</head>
<body>
<div class="canvas">
  <section class="poster">
    <p class="legend">A. = artery<br>V. = vein</p>

    <svg class="vein-figure" role="img" aria-label="Anatomical illustration of a standing human body showing the venous system in blue, with the heart and major vessels" viewBox="0 0 135 725" preserveAspectRatio="none">
      <defs>
        <linearGradient id="figureTone" x1="0" y1="0" x2="1" y2="0">
          <stop offset="0" stop-color="var(--figure-light)"/>
          <stop offset="0.5" stop-color="var(--figure-vein)"/>
          <stop offset="1" stop-color="var(--figure-light)"/>
        </linearGradient>
      </defs>
      <rect x="0" y="0" width="135" height="725" rx="50" fill="url(#figureTone)"/>
    </svg>

    <svg class="leaders" viewBox="0 0 1197 847" aria-hidden="true">
      <g stroke="var(--leader)" stroke-width="0.9" fill="none">
        <!-- right side -->
        <path d="M386 106 330 80"/><path d="M386 122 340 100"/><path d="M386 140 352 140"/>
        <path d="M386 158 345 155"/><path d="M386 177 330 195"/>
        <path d="M439 210 330 215"/><path d="M439 228 350 245"/><path d="M439 245 345 255"/>
        <path d="M439 261 350 270"/><path d="M439 279 335 290"/>
        <path d="M415 295 330 300"/><path d="M415 313 355 310"/><path d="M415 331 325 330"/>
        <path d="M415 349 330 350"/><path d="M415 364 355 355"/><path d="M415 380 345 375"/>
        <path d="M415 397 335 400"/><path d="M415 413 350 415"/><path d="M415 429 355 425"/>
        <path d="M415 445 360 440"/><path d="M415 468 360 470"/><path d="M415 491 355 490"/>
        <path d="M415 513 350 510"/>
        <path d="M402 567 360 565"/><path d="M402 584 355 580"/><path d="M402 600 360 595"/>
        <path d="M402 632 360 630"/><path d="M402 647 355 650"/><path d="M402 665 360 665"/>
        <path d="M402 679 355 680"/><path d="M402 696 355 695"/>
        <path d="M402 735 345 745"/><path d="M402 751 360 750"/><path d="M402 764 375 765"/>
        <!-- left side -->
        <path d="M243 156 300 195"/><path d="M235 171 305 205"/><path d="M227 186 275 215"/>
        <path d="M218 203 265 240"/><path d="M210 220 258 260"/><path d="M203 235 262 275"/>
        <path d="M197 250 285 285"/><path d="M193 265 310 315"/><path d="M185 293 275 300"/>
        <path d="M180 321 300 340"/><path d="M177 338 255 345"/><path d="M176 353 255 365"/>
        <path d="M174 370 252 385"/><path d="M172 396 254 400"/>
        <path d="M136 424 252 450"/><path d="M136 460 252 470"/><path d="M136 490 252 490"/>
      </g>
    </svg>

    <!-- left labels -->
    <div class="label l" style="right:956px;top:150px">Subclavian v.</div>
    <div class="label l" style="right:964px;top:165px">Thoracic internal v.</div>
    <div class="label l" style="right:972px;top:180px">Axillary v.</div>
    <div class="label l" style="right:981px;top:197px">Cephalic v.</div>
    <div class="label l" style="right:989px;top:214px">Brachial v.</div>
    <div class="label l" style="right:996px;top:229px">Basilic v.</div>
    <div class="label l" style="right:1002px;top:244px">Intercostal v.</div>
    <div class="label l" style="right:1006px;top:259px">(Hepatic) portal v.</div>
    <div class="label l" style="right:1014px;top:276px">Thoraco-<br>epigastric v.</div>
    <div class="label l" style="right:1019px;top:304px">Superior and inferior<br>epigastric v.</div>
    <div class="label l" style="right:1022px;top:332px">Median cubital v.</div>
    <div class="label l" style="right:1023px;top:347px">Cephalic v.</div>
    <div class="label l" style="right:1025px;top:364px">Ulnar v.</div>
    <div class="label l" style="right:1027px;top:379px">Median<br>antebrachial v.</div>
    <div class="label l" style="right:1063px;top:407px">Deep<br>palmar<br>arch</div>
    <div class="label l" style="right:1063px;top:443px">Superficial<br>palmar<br>arch</div>
    <div class="label l" style="right:1063px;top:479px">Palmar<br>digital v.</div>

    <!-- right labels -->
    <div class="label" style="left:388px;top:100px">Venous sinuses:</div>
    <div class="label" style="left:388px;top:116px">Sigmoid sinus</div>
    <div class="label" style="left:388px;top:134px">External jugular v.</div>
    <div class="label" style="left:388px;top:152px">Internal jugular v.</div>
    <div class="label" style="left:388px;top:171px">Brachiocefalic trunk</div>
    <div class="label" style="left:441px;top:204px">Superior v. cava</div>
    <div class="label" style="left:441px;top:222px">Pulmonary v.</div>
    <div class="label" style="left:441px;top:239px">Heart</div>
    <div class="label" style="left:441px;top:255px">Coronary a.</div>
    <div class="label" style="left:441px;top:273px">Inferior v. cava</div>
    <div class="label" style="left:417px;top:289px">Hepatic v.</div>
    <div class="label" style="left:417px;top:307px">Splenic v.</div>
    <div class="label" style="left:417px;top:325px">Superior mesenteric v.</div>
    <div class="label" style="left:417px;top:343px">Abdominal v. cava</div>
    <div class="label" style="left:417px;top:358px">Renal v.</div>
    <div class="label" style="left:417px;top:374px">Gonadal v.</div>
    <div class="label" style="left:417px;top:391px">Common iliac v.</div>
    <div class="label" style="left:417px;top:407px">Internal iliac v.</div>
    <div class="label" style="left:417px;top:423px">External iliac v.</div>
    <div class="label" style="left:417px;top:439px">Common femoral v.</div>
    <div class="label" style="left:417px;top:462px">Deep femoral v.</div>
    <div class="label" style="left:417px;top:480px">Subsartorial or<br>superficial femoral v.</div>
    <div class="label" style="left:417px;top:507px">Accessory saphenous v.</div>
    <div class="label" style="left:404px;top:561px">Superior genicular v.</div>
    <div class="label" style="left:404px;top:578px">Popliteal v.</div>
    <div class="label" style="left:404px;top:594px">Inferior genicular v.</div>
    <div class="label" style="left:404px;top:626px">Great saphenous v.</div>
    <div class="label" style="left:404px;top:641px">Small saphenous v.</div>
    <div class="label" style="left:404px;top:659px">Anterior tibial v.</div>
    <div class="label" style="left:404px;top:673px">Posterior tibial v.</div>
    <div class="label" style="left:404px;top:690px">Peroneal v.</div>
    <div class="label" style="left:404px;top:729px">Deep plantar v.</div>
    <div class="label" style="left:404px;top:745px">Dorsal venous arch</div>
    <div class="label" style="left:404px;top:758px">Dorsal digital v.</div>

    <div class="brand">
      <div class="brand-mark"><span class="dot"></span><span>CHRN</span></div>
      <span class="brand-sub">Coastal Harm Reduction<br>Network</span>
    </div>

    <div class="content">
      <p class="kicker">a Guide to</p>
      <h1 class="title one">Clean Practice</h1>
      <h1 class="title two">Manual</h1>

      <h2 class="welcome-head">Welcome to the 2020 revised version of the CHRN Vein Care Guide.</h2>
      <p class="welcome-body">This is a targeted educational resource for people who inject drugs and is not for general distribution under any circumstances. CHRN Vein Care Guide has been created by drug users for drug users to provide information that will help people make informed decisions and reduce the risks of drug related harms.</p>

      <h2 class="section-head" style="top:386px">VEIN CARE AND INJECTING SITES ON THE BODY</h2>
      <p class="small" style="top:411px"><strong>For people who inject drugs, the loss of the most accessible veins can ultimately lead to stark choices:</strong><br>either to stop injecting, switch to another way of using or move to another site on the body where injecting can pose much greater health risks, particularly in relation to blood borne virus (BBV) transmission such as hepatitis C (hep C).</p>
      <p class="small" style="top:454px">The following information is provided to help you make informed decisions about where to inject and how to minimise the risks of BBV transmission as much as possible.</p>

      <div class="checks">
        <span class="check"><svg viewBox="0 0 14 14"><rect x="1" y="2" width="10" height="10" fill="none" stroke="currentColor" stroke-width="1.6"/><path d="M3.5 7l2.5 2.5L13 2" fill="none" stroke="currentColor" stroke-width="1.8"/></svg>Arms</span>
        <span class="check"><svg viewBox="0 0 14 14"><rect x="1" y="2" width="10" height="10" fill="none" stroke="currentColor" stroke-width="1.6"/><path d="M3.5 7l2.5 2.5L13 2" fill="none" stroke="currentColor" stroke-width="1.8"/></svg>Breasts</span>
        <span class="check"><svg viewBox="0 0 14 14"><rect x="1" y="2" width="10" height="10" fill="none" stroke="currentColor" stroke-width="1.6"/><path d="M3.5 7l2.5 2.5L13 2" fill="none" stroke="currentColor" stroke-width="1.8"/></svg>Hands and Fingers</span>
        <span class="check"><svg viewBox="0 0 14 14"><rect x="1" y="2" width="10" height="10" fill="none" stroke="currentColor" stroke-width="1.6"/><path d="M3.5 7l2.5 2.5L13 2" fill="none" stroke="currentColor" stroke-width="1.8"/></svg>Deep Veins</span>
        <span class="check"><svg viewBox="0 0 14 14"><rect x="1" y="2" width="10" height="10" fill="none" stroke="currentColor" stroke-width="1.6"/><path d="M3.5 7l2.5 2.5L13 2" fill="none" stroke="currentColor" stroke-width="1.8"/></svg>Legs</span>
        <span class="check"><svg viewBox="0 0 14 14"><rect x="1" y="2" width="10" height="10" fill="none" stroke="currentColor" stroke-width="1.6"/><path d="M3.5 7l2.5 2.5L13 2" fill="none" stroke="currentColor" stroke-width="1.8"/></svg>Neck</span>
        <span class="check"><svg viewBox="0 0 14 14"><rect x="1" y="2" width="10" height="10" fill="none" stroke="currentColor" stroke-width="1.6"/><path d="M3.5 7l2.5 2.5L13 2" fill="none" stroke="currentColor" stroke-width="1.8"/></svg>Feet</span>
        <span class="check"><svg viewBox="0 0 14 14"><rect x="1" y="2" width="10" height="10" fill="none" stroke="currentColor" stroke-width="1.6"/><path d="M3.5 7l2.5 2.5L13 2" fill="none" stroke="currentColor" stroke-width="1.8"/></svg>Penis</span>
      </div>

      <h2 class="section-head" style="top:635px">VEIN CARE AND THE CIRCULATORY SYSTEM</h2>
      <p class="small" style="top:659px">The circulatory system plays an important role in relation to understanding vein care, blood borne viruses and injecting drug users' health, so it's important to understand how it works and how we can help care for our own systems.</p>
      <p class="small" style="top:694px"><strong>Basics of the circulatory system</strong></p>
      <p class="bullet" style="top:705px">• The circulatory system aids the flow of blood to all tissues in the body;</p>
      <p class="bullet" style="top:726px">• The transfer of oxygen and nutrients between the cells and the blood takes place through microscopic vessels called 'capillaries'; and</p>
      <p class="bullet" style="top:757px">• The heart is the pump that drives this flow of blood to the capillaries in the body's tissues, to facilitate oxygen transfer through the body and then back to the lungs to be re-oxygenated.</p>
    </div>
  </section>
</div>
</body>
</html>
```